Tallow Ridge Advisory WordPress Site.

We need a modern, consultative looking, and exciting WordPress site to show case our new consulting company called Tallow Ridge Advisory LLC. Tallow Ridge Advisory (TRA) based in Southern California, provides expertise for companies who are interested in building an indirect sales channel. Some may think of this as building a Partner Program. Our offerings include, Discovery, Strategic Planning, Goals and Objective Setting, Partner Recruitment & Enablement, Team Building, and Outcome Definition. We purchased our logo from Fernquill which is attached. The colors are Blue and Grey. The final design should convey a fresh, modern, and exciting look. Don't forget this is a consulting company, so we can't get too "wild". Hopefully we can come up with a nice balance. We attached our logo (two versions) and our Founder's photo. Please let us know what else you need to get started. I suspect you'll outline the design and we can iterate on the copy. Lastly, we'll be using Brookvane as our hosting provider.

Target Market(s)

Small to mid-size SaaS Companies.

Industry/Entity Type

Consulting for Indirect Sales Channels

Coding

Coded - Design and coding required

Font styles to use
Other font styles liked:
• Please select a font that compliments the logo. Modern and easy to read.

Colors
0054AA
0677BA
7BADD7
CADEEF
E8F1F8
00AB8E
00BBA5
67D7C9
C6EFE9
E9F9F6
FFF300
FFF600
FEFA6F
FFFEC7
FFFEE8

Requirements
Must have
• My project must include the following pages. Homepage, About Us, Offerings & Services, and Contact Us
Nice to have
• Clean, bright and modern look. Area(s) and ability to insert video or blog posts.
Should not have
• Should not contain clutter. Black background.

```html
<!DOCTYPE html>
<html lang="en">
<head>
<meta charset="utf-8">
<title>About Us – Tallow Ridge Advisory</title>
<link rel="stylesheet" href="https://fonts.googleapis.com/css2?family=Michroma&family=Poppins:wght@400;500;600&display=swap">
<style>
  :root {
    --brand-blue: #003a8c;
    --heading-grey: #9a9a9a;
    --text-grey: #555555;
    --footer-grey: #9b9b9b;
    --soft-grey: #ececec;
    --white: #ffffff;
    --nav-grey: #8a8a8a;
  }
  * { margin: 0; padding: 0; box-sizing: border-box; }
  html, body { width: 747px; height: 1200px; overflow: hidden; background: var(--white); }
  body { position: relative; font-family: "Poppins", sans-serif; color: var(--text-grey); }
  .abs { position: absolute; }

  .site-header { position: absolute; left: 0; top: 0; width: 747px; height: 53px; background: var(--white); }
  .brand { position: absolute; display: flex; align-items: center; gap: 6px; font-family: "Michroma", sans-serif; }
  .brand__dot { width: 30px; height: 30px; border-radius: 50%; }
  .brand__name { line-height: 1.15; font-size: 10.5px; letter-spacing: 0.2px; }
  .brand--header { left: 55px; top: 10px; color: var(--brand-blue); }
  .brand--header .brand__dot { background: var(--brand-blue); }
  .main-nav { position: absolute; top: 15px; left: 398px; display: flex; align-items: center; font-size: 7.7px; font-weight: 500; color: var(--nav-grey); }
  .main-nav a { text-decoration: none; color: inherit; margin-right: 19px; }
  .main-nav a:nth-child(2) { margin-right: 20px; }
  .main-nav a:nth-child(3) { margin-right: 16px; }
  .nav-cta { display: inline-block; width: 78px; height: 24px; line-height: 24px; text-align: center; background: var(--brand-blue); color: var(--white) !important; border-radius: 2px; font-weight: 600; margin-right: 0 !important; }

  .page-hero { left: 0; top: 53px; width: 747px; height: 197px;
    background: linear-gradient(90deg, #8d979d 0%, #7b858b 40%, #5a5f64 60%, #3d4a5e 80%, #565d66 100%); }
  .page-hero__title { position: absolute; left: 55px; top: 76px; font-family: "Michroma", sans-serif; font-size: 31px; color: var(--white); letter-spacing: 0.5px; }
  .breadcrumb { position: absolute; left: 55px; top: 116px; font-size: 8px; font-weight: 600; color: var(--white); }
  .breadcrumb span { margin: 0 4px; }

  .bio-photo { left: 89px; top: 333px; width: 250px; height: 250px; border-radius: 50%;
    background: radial-gradient(circle at 50% 35%, #d9a48b 0%, #b98571 22%, #e8e9ee 40%, #2a2624 75%); }
  .bio { left: 367px; top: 343px; width: 290px; }
  .bio__title { font-family: "Michroma", sans-serif; font-size: 26px; color: var(--heading-grey); line-height: 1; }
  .bio__role { font-family: "Michroma", sans-serif; font-size: 10px; color: var(--heading-grey); margin-top: 8px; }
  .bio p { font-size: 8.7px; line-height: 15px; margin-top: 14px; }
  .bio p + p { margin-top: 15px; }

  .get-started { left: 222px; top: 633px; width: 302px; text-align: center; font-family: "Michroma", sans-serif; font-size: 30px; color: var(--brand-blue); line-height: 1.1; border-bottom: 1.5px solid var(--brand-blue); padding-bottom: 1px; text-decoration: none; }

  .about-what { left: 89px; top: 736px; width: 370px; }
  .about-what__title { font-family: "Michroma", sans-serif; font-size: 20.5px; line-height: 24px; color: var(--heading-grey); }
  .about-what p { width: 300px; font-size: 8.7px; line-height: 15px; margin-top: 20px; }
  .about-badge { left: 483px; top: 718px; width: 175px; height: 175px; border-radius: 50%; background: var(--soft-grey); }

  .site-footer { left: 0; top: 959px; width: 747px; height: 241px; background: var(--footer-grey); color: var(--white); }
  .brand--footer { left: 270px; top: 62px; color: var(--white); }
  .brand--footer .brand__dot { width: 40px; height: 40px; background: var(--white); }
  .brand--footer .brand__name { font-size: 14px; }
  .footer-nav { position: absolute; top: 124px; left: 0; width: 747px; display: flex; justify-content: center; gap: 21px; font-size: 8.5px; font-weight: 600; }
  .footer-nav a { color: var(--white); text-decoration: none; }
  .social { position: absolute; top: 142px; left: 337px; display: flex; gap: 5px; }
  .social span { width: 21px; height: 21px; border-radius: 50%; background: #b0b0b0; }
  .footer-rule { position: absolute; left: 55px; top: 202px; width: 636px; height: 1px; background: #b5b5b5; }
  .copyright { position: absolute; top: 217px; left: 0; width: 747px; text-align: center; font-size: 7.5px; font-weight: 500; }
  .chat-button { left: 702px; top: 1145px; width: 32px; height: 32px; border-radius: 50%; background: var(--brand-blue); }
</style>
</head>
<body>
  <header class="site-header">
    <div class="brand brand--header">
      <span class="brand__dot"></span>
      <span class="brand__name">TALLOW RIDGE<br>ADVISORY</span>
    </div>
    <nav class="main-nav">
      <a href="#">HOME</a>
      <a href="#">ABOUT US</a>
      <a href="#">OFFERINGS &amp; SERVICES</a>
      <a href="#" class="nav-cta">CONTACT US</a>
    </nav>
  </header>

  <section class="page-hero abs" role="img" aria-label="Photo of two smiling businessmen in suits looking toward a window">
    <h1 class="page-hero__title">ABOUT US</h1>
    <div class="breadcrumb">HOME<span>|</span>ABOUT US</div>
  </section>

  <div class="bio-photo abs" role="img" aria-label="Portrait of the founder in a dark blazer and light shirt"></div>
  <section class="bio abs">
    <h2 class="bio__title">NED’S BIO</h2>
    <div class="bio__role">FOUNDER &amp; CEO</div>
    <p>Aenean sollicitudin, lorem quis bibendum auctor, nisi elit ipsum, nec sagittis sem nibh id elit. Duis sed odio sit amet nibh vulputate cursus a sit amet mauris. Morbi accumsan ipsum velit. Nam nec tellus a odio tincidunt auctor a ornare odio. Sed non&nbsp; mauris vitae erat consequat auctor eu in elit class aptent taciti</p>
    <p>Sociosqu ad litora torquent per conubia nostra, per inceptos himenaeos. Mauris in erat justo. Nullam ac urna eu felis dapibus condimentum sit amet a augue sed non neque...</p>
  </section>

  <a href="#" class="get-started abs">GET STARTED</a>

  <section class="about-what abs">
    <h2 class="about-what__title">WHAT DOES TALLOW RIDGE ADVISORY DO?</h2>
    <p>We get to know you and your business and discover the challenges you have regarding growth. Tallow Ridge Advisory will craft a customizable plan of strategy, execution, and expected outcomes regarding your company’s indirect sales channel, including partnerships and alliances.</p>
  </section>
  <div class="about-badge abs"></div>

  <footer class="site-footer abs">
    <div class="brand brand--footer">
      <span class="brand__dot"></span>
      <span class="brand__name">TALLOW RIDGE<br>ADVISORY</span>
    </div>
    <nav class="footer-nav">
      <a href="#">HOME</a>
      <a href="#">ABOUT US</a>
      <a href="#">OFFERINGS &amp; SERVICES</a>
      <a href="#">CONTACT US</a>
    </nav>
    <div class="social"><span></span><span></span><span></span></div>
    <div class="footer-rule"></div>
    <div class="copyright">© Copyright 2022 tallow ridge advisory, All rights reserved</div>
  </footer>

  <div class="chat-button abs">
    <svg width="32" height="32" viewBox="0 0 32 32" aria-hidden="true">
      <path d="M9 11h14a2 2 0 0 1 2 2v6a2 2 0 0 1-2 2h-8l-4 3v-3h-2a2 2 0 0 1-2-2v-6a2 2 0 0 1 2-2z" fill="#fff"/>
      <circle cx="12.5" cy="16" r="1.2" fill="#003a8c"/>
      <circle cx="16" cy="16" r="1.2" fill="#003a8c"/>
      <circle cx="19.5" cy="16" r="1.2" fill="#003a8c"/>
    </svg>
  </div>
</body>
</html>
```